Marabel Tovinski - Business Cards

Hello everyone,

I need business cards designed to the following specs:

3.5"x2" with .25" bleed all around for printing
Square corners only

Please use attached business card for design reference.

Front:

Marabel Tovinski
Sales Associate

555-214-7093
maratovi7@ [login to view URL] (no space)
IG logo @agentmarabel
4820 SW 87th Ave, Ste #210
Miami, Lakes, FL 33099

Back:

Harborlane logo

Please submit editable AI, PDF, and JPG files.

Thanks and good luck!!!

```html
<!DOCTYPE html>
<html lang="en">
<head>
<meta charset="utf-8">
<title>Marabel Tovinski – Business Cards</title>
<link href="https://fonts.googleapis.com/css2?family=Montserrat:wght@400;600;800&display=swap" rel="stylesheet">
<style>
  :root {
    --page-bg: #e9e6e2;
    --card-bg: #f8f7f9;
    --ink: #111111;
    --ink-soft: #2a2a2a;
    --rule: #1a1a1a;
    --photo-top: #cfcccc;
    --photo-bottom: #2b2b2d;
  }
  * { box-sizing: border-box; margin: 0; padding: 0; }
  html, body {
    width: 1200px; height: 885px; overflow: hidden;
    background: var(--page-bg);
    font-family: "Montserrat", sans-serif;
    color: var(--ink);
  }
  .sheet {
    position: relative; width: 1200px; height: 885px;
    display: flex; flex-direction: column; align-items: center; justify-content: center; gap: 50px;
  }
  .card {
    position: relative; width: 660px; height: 377px;
    background: var(--card-bg);
    box-shadow: 0 6px 18px rgba(0,0,0,.18);
    overflow: hidden;
  }

  /* Back: company name */
  .brand {
    position: absolute; left: 50%; top: 50%; transform: translate(-50%, -50%);
    display: flex; align-items: center; gap: 14px;
    white-space: nowrap;
  }
  .brand-marker { width: 22px; height: 22px; background: var(--ink); flex: none; }
  .brand-name { font-weight: 600; font-size: 30px; color: var(--ink); line-height: 1; }

  /* Front: agent details */
  .portrait {
    position: absolute; left: 120px; top: 150px; width: 260px; height: 227px;
    background: linear-gradient(180deg, var(--photo-top) 0%, var(--photo-bottom) 40%, var(--photo-bottom) 100%);
  }
  .agent-id { position: absolute; right: 40px; top: 44px; text-align: right; }
  .agent-name {
    font-weight: 800; font-size: 21px; letter-spacing: .6px; text-transform: uppercase;
    padding-bottom: 6px; border-bottom: 1.5px solid var(--rule); padding-left: 40px;
  }
  .agent-title { margin-top: 5px; font-weight: 400; font-size: 13px; color: var(--ink-soft); padding-right: 46px; }
  .office-address {
    position: absolute; right: 40px; top: 138px; text-align: right;
    font-style: normal; font-size: 14px; line-height: 1.5; font-weight: 400; color: var(--ink-soft);
  }
  .contact-list {
    position: absolute; right: 40px; top: 205px; list-style: none; text-align: right;
    font-size: 14px; line-height: 1.7; color: var(--ink-soft);
  }
  .contact-list li { display: flex; justify-content: flex-end; align-items: center; gap: 6px; }
  .contact-list svg { width: 12px; height: 12px; flex: none; }
  .social-marker { width: 10px; height: 10px; border: 1.5px solid var(--ink); display: inline-block; flex: none; }
</style>
</head>
<body>
<main class="sheet">
  <section class="card card--back" aria-label="Card back">
    <div class="brand">
      <span class="brand-marker" aria-hidden="true"></span>
      <span class="brand-name">Harborlane International Realty</span>
    </div>
  </section>

  <section class="card card--front" aria-label="Card front">
    <div class="portrait" role="img" aria-label="Portrait photo of the sales associate"></div>
    <div class="agent-id">
      <h1 class="agent-name">Marabel Tovinski</h1>
      <p class="agent-title">Sales Associate</p>
    </div>
    <address class="office-address">
      4820 SW 87th Ave, Ste #210<br>Miami, Lakes, FL 33099
    </address>
    <ul class="contact-list">
      <li>555-214-7093
        <svg viewBox="0 0 24 24" aria-hidden="true"><path fill="var(--ink)" d="M6.6 10.8a15 15 0 0 0 6.6 6.6l2.2-2.2a1 1 0 0 1 1-.25 11.4 11.4 0 0 0 3.6.57 1 1 0 0 1 1 1V20a1 1 0 0 1-1 1A17 17 0 0 1 3 4a1 1 0 0 1 1-1h3.5a1 1 0 0 1 1 1c0 1.25.2 2.45.57 3.6a1 1 0 0 1-.25 1z"/></svg>
      </li>
      <li>maratovi7@ postmail.net
        <svg viewBox="0 0 24 24" aria-hidden="true"><rect x="2" y="5" width="20" height="14" fill="var(--ink)"/><path d="M2 5l10 8 10-8" fill="none" stroke="var(--card-bg)" stroke-width="2"/></svg>
      </li>
      <li>@agentmarabel <span class="social-marker" aria-hidden="true"></span></li>
    </ul>
  </section>
</main>
</body>
</html>
```